Len Morvath

I am the director of Casa Del Humo International. We make premium cigars

I want an insanely beautiful card that directly attracts attention. Do your best. The card can use emboss, foil, laser-cut metal or anything else. Make it stand out, but also elegant.

Target Market(s)

Cigar Distributors

Industry/Entity Type

Cigars

Contact Information for Business Card

Email: len.morvath@morvaths.com + Logos (attached) + Position: Director + 'High-End Cigars'

Colors

Designer to choose colors to be used in the design.

Requirements
Nice to have
• Please check us out at www.casadelhumo.com and try to use our colors and styles

```html
<!DOCTYPE html>
<html lang="en">
<head>
<meta charset="UTF-8">
<title>Casa Del Humo International — Business Card</title>
<link rel="stylesheet" href="https://fonts.googleapis.com/css2?family=EB+Garamond:wght@500&family=Arimo:wght@400;700&display=swap">
<style>
  :root {
    --backdrop: #d3d4d6;
    --card-black: #0f0f0f;
    --card-white: #ffffff;
    --accent-red: #b31f1d;
    --ink-dark: #151515;
    --ink-light: #f4f4f4;
    --serif: "EB Garamond", "Times New Roman", serif;
    --sans: "Arimo", Arial, sans-serif;
  }
  * { box-sizing: border-box; margin: 0; padding: 0; }
  html, body {
    width: 1200px; height: 800px; overflow: hidden;
    background: var(--backdrop);
  }
  .canvas {
    width: 1200px; height: 800px;
    display: flex; align-items: center; justify-content: center; gap: 40px;
  }
  .card {
    position: relative;
    width: 540px; height: 308px;
    border-bottom: 3px solid var(--accent-red);
    border-right: 2px solid var(--accent-red);
    box-shadow: 0 18px 30px rgba(0,0,0,0.22);
    overflow: hidden;
  }
  .card--front { background: var(--card-black); color: var(--ink-light); }
  .card--back { background: var(--card-white); color: var(--ink-dark); }

  .company-name {
    position: absolute; left: 0; right: 0;
    text-align: center;
    font-family: var(--sans); font-weight: 400;
    font-size: 26px; letter-spacing: 1px;
    white-space: nowrap;
  }
  .location {
    position: absolute; left: 0; right: 0; text-align: center;
    font-family: var(--sans); font-size: 15px; letter-spacing: 0.6px;
  }
  .card--front .company-name { top: 100px; }
  .card--front .location { top: 152px; }
  .tagline {
    position: absolute; left: 0; right: 0; top: 204px; text-align: center;
    font-family: var(--sans); font-weight: 700; font-size: 14px;
    letter-spacing: 1.2px; color: var(--accent-red);
  }

  .card--back .company-name { top: 40px; }
  .card--back .location { top: 90px; }

  .person {
    position: absolute; left: 44px; bottom: 48px;
  }
  .person__name {
    font-family: var(--serif); font-size: 30px; font-weight: 500; line-height: 1;
  }
  .person__role {
    margin-top: 4px;
    font-family: var(--sans); font-size: 15px; color: var(--accent-red);
  }
  .contact {
    position: absolute; right: 34px; top: 156px;
    list-style: none;
    font-family: var(--sans); font-size: 13px;
  }
  .contact__item { display: flex; align-items: center; gap: 9px; margin-bottom: 9px; }
  .contact__icon { width: 16px; height: 16px; flex: none; }
</style>
</head>
<body>
<main class="canvas">

  <section class="card card--front" aria-label="Card front">
    <h1 class="company-name">Casa Del Humo International</h1>
    <p class="location">SOLANA - MAREVIA</p>
    <p class="tagline">HIGH-END CIGARS</p>
  </section>

  <section class="card card--back" aria-label="Card back">
    <h2 class="company-name">Casa Del Humo International</h2>
    <p class="location">SOLANA - MAREVIA</p>

    <ul class="contact">
      <li class="contact__item">
        <svg class="contact__icon" viewBox="0 0 16 16" aria-hidden="true">
          <rect x="1" y="3" width="14" height="10" rx="1" fill="var(--accent-red)"/>
          <polyline points="1.5,4 8,9 14.5,4" fill="none" stroke="#fff" stroke-width="1.3"/>
        </svg>
        <span>len.morvath@morvaths.com</span>
      </li>
      <li class="contact__item">
        <svg class="contact__icon" viewBox="0 0 16 16" aria-hidden="true">
          <circle cx="8" cy="8" r="6.5" fill="none" stroke="var(--accent-red)" stroke-width="1.4"/>
          <ellipse cx="8" cy="8" rx="2.8" ry="6.5" fill="none" stroke="var(--accent-red)" stroke-width="1.1"/>
          <line x1="1.5" y1="8" x2="14.5" y2="8" stroke="var(--accent-red)" stroke-width="1.1"/>
        </svg>
        <span>www.casadelhumo.com</span>
      </li>
    </ul>

    <div class="person">
      <p class="person__name">Len Morvath</p>
      <p class="person__role">Director</p>
    </div>
  </section>

</main>
</body>
</html>
```